professional business card

Professional business card with logo on one side, and underneath logo list:
- power
-data
-fibre optic
-isolar

On other side:
Marcus Webb
Owner
MOB 0432 958 720
marcus@vorn.com.au
www.vornelectrical.com.au

Please edit logo to just leave VORN

```html
<!DOCTYPE html>
<html lang="en">
<head>
<meta charset="utf-8">
<title>VORN Electrical – Business Card</title>
<link href="https://fonts.googleapis.com/css2?family=Arimo:wght@400&family=Montserrat:wght@600&display=swap" rel="stylesheet">
<style>
  :root {
    --page: #fdfdfd;
    --card: #231f20;
    --band: #1a1817;
    --shadow: #d3d3d3;
    --teal: #049e9f;
    --grey: #808080;
  }
  html, body {
    margin: 0;
    width: 1200px;
    height: 1200px;
    overflow: hidden;
    background: var(--page);
  }
  .canvas { position: relative; width: 1200px; height: 1200px; }
  .card-shadow {
    position: absolute;
    left: 88px; top: 278px;
    width: 1058px; height: 605px;
    background: var(--shadow);
  }
  .card {
    position: absolute;
    left: 76px; top: 266px;
    width: 1058px; height: 605px;
    background: var(--card);
    overflow: hidden;
    font-family: "Arimo", Arial, sans-serif;
  }
  .card-bands { position: absolute; inset: 0; }
  .brand-name {
    position: absolute;
    left: 28px; top: 5px;
    margin: 0;
    font-family: "Montserrat", Arial, sans-serif;
    font-weight: 600;
    font-size: 172px;
    line-height: 1;
    letter-spacing: -2px;
    color: var(--teal);
  }
  .services {
    position: absolute;
    left: 29px; top: 311px;
    margin: 0; padding: 0;
    list-style: none;
    color: var(--teal);
    font-size: 57px;
    line-height: 69px;
    letter-spacing: -1px;
  }
  .contact {
    position: absolute;
    right: 44px; top: 290px;
    margin: 0;
    text-align: right;
    color: var(--grey);
    font-size: 47px;
    line-height: 56.3px;
    font-style: normal;
  }
  .contact p { margin: 0; }
</style>
</head>
<body>
<div class="canvas">
  <div class="card-shadow"></div>
  <section class="card" aria-label="VORN Electrical business card">
    <svg class="card-bands" viewBox="0 0 1058 605" width="1058" height="605" aria-hidden="true">
      <polygon fill="var(--band)" points="205,0 362,0 94,302 362,605 205,605 0,371 0,234"/>
      <rect fill="var(--band)" x="1039" y="0" width="19" height="605"/>
    </svg>
    <h1 class="brand-name">VORN</h1>
    <ul class="services">
      <li>POWER</li>
      <li>DATA</li>
      <li>FIBRE OPTIC</li>
      <li>ISOLAR</li>
    </ul>
    <address class="contact">
      <p class="contact-name">Marcus Webb</p>
      <p class="contact-role">Owner</p>
      <p class="contact-phone">MOB 0432 958 720</p>
      <p class="contact-email">marcus@vorn.com.au</p>
      <p class="contact-web">www.vornelectrical.com.au</p>
    </address>
  </section>
</div>
</body>
</html>
```